Postcard Design

We'd like a postcard designed for our Crate O' Crunch subscription company. Our website is crateocrunch.example and we offer a monthly subscription box of snacks.
We'd like the final design to pop and offer engagement via social media etc. #crateocrunch is a hashtag we'd like used.
attached is our logo.
Updates

Please use the #crateocrunch as follows. "Take A Picture Of Your Crate O' Crunch To Be Featured On Our Site, And Have A Chance To Win A Free Month Of Snacks!"

Target Market(s)

College students, moms, kids.
People who love snacks.

Industry/Entity Type

It Company

Requirements
Must have
• Please use the #crateocrunch as follows.
"Take A Picture Of Your Crate O' Crunch And Use #CRATEOCRUNCH To Be Featured On Our Site, And Have A Chance To Win A Free Month Of Snacks!"

```html
<!DOCTYPE html>
<html lang="en">
<head>
<meta charset="utf-8">
<title>Crate O' Crunch Postcard</title>
<link rel="stylesheet" href="https://fonts.googleapis.com/css2?family=Montserrat:wght@300;700;800&family=Roboto+Condensed:wght@700&display=swap">
<style>
  :root {
    --cardboard: #c39a6b;
    --cardboard-light: #d2ad80;
    --cardboard-dark: #a97f52;
    --paper: #ffffff;
    --paper-shade: #e9e9e9;
    --teal: #6ccbd3;
    --orange: #d8642a;
    --ink-white: #ffffff;
    --social: #3f6fb0;
    --photo-light: #e6e2df;
    --photo-mid: #b9b1ad;
  }
  * { box-sizing: border-box; margin: 0; padding: 0; }
  html, body { width: 1200px; height: 930px; overflow: hidden; }
  .postcard {
    position: relative;
    width: 1200px;
    height: 930px;
    overflow: hidden;
    background:
      radial-gradient(ellipse at 30% 20%, var(--cardboard-light), transparent 60%),
      radial-gradient(ellipse at 80% 75%, var(--cardboard-light), transparent 55%),
      linear-gradient(160deg, var(--cardboard) 0%, var(--cardboard-dark) 100%);
    font-family: "Montserrat", Arial, sans-serif;
  }
  .intro {
    position: absolute;
    left: 30px;
    top: 14px;
    color: var(--ink-white);
    text-transform: uppercase;
    font-size: 30px;
    line-height: 37px;
    letter-spacing: 0.5px;
  }
  .intro .lead { font-weight: 800; display: block; }
  .intro .charity { font-weight: 300; display: block; font-size: 31px; letter-spacing: 3px; }
  .torn-band { position: absolute; left: 0; top: 270px; width: 1200px; height: 370px; }
  .steps {
    position: absolute;
    left: 0; top: 298px;
    width: 1200px;
    height: 300px;
  }
  .step {
    position: absolute;
    width: 330px;
    text-align: center;
  }
  .step:nth-child(1) { left: 67px; }
  .step:nth-child(2) { left: 390px; }
  .step:nth-child(3) { left: 742px; }
  .step-icon {
    display: block;
    width: 190px;
    height: 190px;
    margin: 0 auto;
  }
  .step-caption {
    margin-top: 40px;
    font-family: "Roboto Condensed", Arial, sans-serif;
    font-weight: 700;
    color: var(--orange);
    text-transform: uppercase;
    font-size: 25px;
    line-height: 32px;
  }
  .social {
    position: absolute;
    left: 55px;
    top: 740px;
    display: flex;
    gap: 30px;
  }
  .social-item {
    display: flex;
    align-items: center;
    gap: 10px;
    color: var(--ink-white);
    font-weight: 700;
    font-size: 22px;
  }
  .social-item .mark { width: 40px; height: 40px; background: var(--social); }
  .base-strip {
    position: absolute;
    left: 0; top: 848px;
    width: 1200px; height: 82px;
    background: var(--paper);
  }
  .treat-photo {
    position: absolute;
    left: 787px; top: 675px;
    width: 413px; height: 255px;
    background: linear-gradient(160deg, var(--photo-light) 0%, var(--photo-mid) 100%);
  }
</style>
</head>
<body>
<main class="postcard">
  <p class="intro">
    <span class="lead">When you sign up for Crate O' Crunch,<br>every month you will receive a box<br>of carefully selected delicious<br>snacks and munchies.</span>
    <span class="charity">10% of every sale will go to a charitable cause.</span>
  </p>

  <svg class="torn-band" viewBox="0 0 1200 370" aria-hidden="true">
    <path fill="var(--paper-shade)" d="M0 30 L60 20 L130 34 L210 14 L300 28 L380 8 L470 26 L560 12 L650 30 L740 10 L830 24 L920 6 L1010 22 L1100 12 L1200 26 L1200 350 L1120 340 L1040 360 L950 338 L860 356 L770 334 L680 352 L590 330 L500 350 L410 332 L320 354 L230 336 L140 356 L60 340 L0 352 Z"/>
    <path fill="var(--paper)" d="M0 40 L70 30 L140 44 L220 24 L310 38 L390 18 L480 36 L570 22 L660 40 L750 20 L840 34 L930 16 L1020 32 L1110 22 L1200 36 L1200 340 L1120 330 L1040 348 L950 328 L860 344 L770 324 L680 342 L590 320 L500 338 L410 322 L320 342 L230 326 L140 344 L60 330 L0 342 Z"/>
  </svg>

  <section class="steps">
    <div class="step">
      <svg class="step-icon" viewBox="0 0 180 180" aria-hidden="true">
        <circle cx="90" cy="90" r="90" fill="var(--teal)"/>
        <rect x="40" y="58" width="100" height="70" rx="12" fill="var(--orange)" stroke="#fff" stroke-width="4"/>
        <rect x="52" y="48" width="24" height="12" rx="3" fill="var(--orange)" stroke="#fff" stroke-width="4"/>
        <circle cx="90" cy="93" r="24" fill="#fff"/>
        <circle cx="90" cy="93" r="17" fill="var(--orange)"/>
        <circle cx="90" cy="93" r="10" fill="#fff"/>
      </svg>
      <p class="step-caption">Take a picture<br>of your Crate O' Crunch</p>
    </div>
    <div class="step">
      <svg class="step-icon" viewBox="0 0 180 180" aria-hidden="true">
        <circle cx="90" cy="90" r="90" fill="var(--teal)"/>
        <rect x="38" y="45" width="104" height="76" rx="6" fill="var(--orange)" stroke="#fff" stroke-width="4"/>
        <rect x="48" y="55" width="84" height="56" fill="var(--teal)" stroke="#fff" stroke-width="3"/>
        <rect x="80" y="121" width="20" height="12" fill="var(--orange)" stroke="#fff" stroke-width="3"/>
        <rect x="62" y="132" width="56" height="8" rx="3" fill="var(--orange)" stroke="#fff" stroke-width="3"/>
      </svg>
      <p class="step-caption">Use #CRATEOCRUNCH to be<br>featured on our site</p>
    </div>
    <div class="step">
      <svg class="step-icon" viewBox="0 0 180 180" aria-hidden="true">
        <circle cx="90" cy="90" r="90" fill="var(--teal)"/>
        <path d="M58 44 H122 V70 C122 92 108 104 90 104 C72 104 58 92 58 70 Z" fill="var(--orange)" stroke="#fff" stroke-width="4"/>
        <path d="M58 54 H42 C42 76 50 84 62 86 M122 54 H138 C138 76 130 84 118 86" fill="none" stroke="#fff" stroke-width="5"/>
        <rect x="82" y="104" width="16" height="18" fill="var(--orange)" stroke="#fff" stroke-width="3"/>
        <rect x="64" y="120" width="52" height="18" rx="3" fill="var(--orange)" stroke="#fff" stroke-width="4"/>
      </svg>
      <p class="step-caption">Have a chance to win a<br>free month of snacks!</p>
    </div>
  </section>

  <nav class="social" aria-label="Social channels">
    <span class="social-item"><span class="mark"></span>Friendspace</span>
    <span class="social-item"><span class="mark"></span>Chirply</span>
    <span class="social-item"><span class="mark"></span>Snapgrid</span>
  </nav>

  <div class="base-strip"></div>
  <div class="treat-photo" role="img" aria-label="Photo of a chocolate sandwich cookie splashing into milk"></div>
</main>
</body>
</html>
```